Flyers for social media company

To create a postcard sized flyer to send to potential clients informing them of our business and what we can offer.

We are a social media company offering clients web design, social media management on a number of platforms.

Would be nice to have our Teal Heron surrounded by a number of yellow ducks so the blue stand out from the crowd.

Business

```html
<!DOCTYPE html>
<html lang="en">
<head>
<meta charset="utf-8">
<title>Teal Heron – Social Media Management Flyer</title>
<link href="https://fonts.googleapis.com/css2?family=Montserrat:wght@300;400;600;700&family=Open+Sans:wght@400;600&display=swap" rel="stylesheet">
<style>
  :root {
    --navy: #3c4a66;
    --navy-deep: #2a3245;
    --navy-bar: #354159;
    --sky: #4f8fd0;
    --sky-soft: #cfe2f1;
    --sky-faint: #e3eef7;
    --strip: #4d6f9c;
    --ink: #2f3440;
    --white: #ffffff;
  }
  * { margin: 0; padding: 0; box-sizing: border-box; }
  html, body { width: 800px; height: 1200px; overflow: hidden; background: var(--white); }
  .flyer {
    position: relative;
    width: 800px;
    height: 1200px;
    overflow: hidden;
    background: var(--white);
    font-family: "Open Sans", Arial, sans-serif;
  }
  .backdrop { position: absolute; inset: 0; }
  .top-bar {
    position: absolute; left: 79px; top: 14px;
    width: 665px; height: 28px; background: var(--navy-bar);
  }
  .hero-art {
    position: absolute; left: 85px; top: 100px;
    width: 323px; height: 294px;
    border-radius: 18px;
    background: radial-gradient(circle at 50% 40%, #f2f6fa 0%, #b9d3ea 45%, #4f7fb3 80%, #3c4a66 100%);
  }
  .brand {
    position: absolute; left: 420px; top: 160px; width: 330px;
    text-align: center; color: var(--sky);
    font-family: "Montserrat", sans-serif;
  }
  .brand-name {
    display: block;
    font-weight: 300; font-size: 76px; line-height: 0.98; letter-spacing: 2px;
  }
  .brand-tag {
    display: block; margin-top: 8px;
    font-weight: 600; font-size: 15px; letter-spacing: 1px; color: var(--ink);
  }
  .promise {
    position: absolute; left: 60px; top: 440px; width: 680px;
    text-align: center; color: var(--ink);
    font-size: 24px; line-height: 1.3;
  }
  .about {
    position: absolute; left: 0; top: 563px; width: 800px; height: 510px;
    background: var(--navy); color: var(--white);
  }
  .about-shape { position: absolute; left: 0; top: 0; }
  .about-content { position: absolute; left: 99px; top: 105px; width: 610px; }
  .section-title {
    font-family: "Montserrat", sans-serif; font-weight: 400;
    font-size: 42px; letter-spacing: 9px; line-height: 1;
    padding-bottom: 12px; border-bottom: 3px solid var(--white);
  }
  .section-text { margin-top: 16px; font-size: 21px; line-height: 1.22; }
  .subtitle {
    margin-top: 42px;
    font-family: "Montserrat", sans-serif; font-weight: 400;
    font-size: 40px; line-height: 1;
    padding-bottom: 12px; border-bottom: 3px solid var(--white);
  }
  .footer {
    position: absolute; left: 0; top: 1073px; width: 800px; height: 127px;
    background: var(--navy-deep); color: var(--white);
    display: flex; align-items: center; justify-content: center; gap: 24px;
  }
  .footer-brand { display: flex; align-items: center; gap: 14px; }
  .footer-mark { width: 62px; height: 62px; border-radius: 50%; background: var(--sky); }
  .footer-name {
    font-family: "Montserrat", sans-serif; font-weight: 700;
    font-size: 30px; line-height: 1; color: var(--white);
  }
  .footer-divider { width: 3px; height: 70px; background: var(--white); }
  .contact { font-family: "Montserrat", sans-serif; }
  .contact-phone { font-weight: 700; font-size: 30px; line-height: 1.1; }
  .contact-label { font-weight: 600; font-size: 17px; letter-spacing: 1px; }
</style>
</head>
<body>
<main class="flyer">
  <svg class="backdrop" width="800" height="563" viewBox="0 0 800 563" aria-hidden="true">
    <circle cx="230" cy="180" r="210" fill="var(--sky-faint)"/>
    <circle cx="60" cy="150" r="70" fill="var(--sky-soft)" opacity="0.7"/>
    <circle cx="690" cy="70" r="110" fill="var(--sky-faint)"/>
    <circle cx="760" cy="260" r="80" fill="var(--sky-soft)" opacity="0.6"/>
    <circle cx="110" cy="470" r="90" fill="var(--sky-faint)"/>
    <circle cx="640" cy="520" r="120" fill="var(--sky-faint)"/>
  </svg>

  <div class="top-bar"></div>

  <div class="hero-art" role="img" aria-label="Illustration of a laptop with a cloud, chat bubbles, a globe and envelopes"></div>

  <h1 class="brand">
    <span class="brand-name">TEAL<br>HERON</span>
    <span class="brand-tag">SOCIAL MEDIA MANAGEMENT</span>
  </h1>

  <p class="promise">We are always ready to give you an excellent service.<br>That's why we are your best alternative.</p>

  <section class="about">
    <svg class="about-shape" width="800" height="100" viewBox="0 0 800 100" aria-hidden="true">
      <rect x="0" y="0" width="800" height="28" fill="var(--strip)"/>
      <polygon points="560,0 690,0 690,78" fill="var(--white)"/>
    </svg>
    <div class="about-content">
      <h2 class="section-title">ABOUT US</h2>
      <p class="section-text">We are a social networking company that offers web design and social network administration services on several platforms.</p>
      <h3 class="subtitle">We offer you a quality service</h3>
      <p class="section-text">Our goal is for the customer to be 100% satisfied. That's why we treat you like at home!</p>
    </div>
  </section>

  <footer class="footer">
    <div class="footer-brand">
      <span class="footer-mark" aria-hidden="true"></span>
      <span class="footer-name">TEAL HERON</span>
    </div>
    <span class="footer-divider" aria-hidden="true"></span>
    <div class="contact">
      <div class="contact-phone">1-800-555-0147</div>
      <div class="contact-label">CONTACT US</div>
    </div>
  </footer>
</main>
</body>
</html>
```